Scrap Metal Company Require Brochure for presentation to prospective client

We are a scrap metal company based in Singapore.
We require a brochure of about 4 pages, 1) Cover Page, 2 and 3 is the material we deal in and services we provide and 4) a backpage.
Brochure will be presented to prospective and selected local supplier to present to them the type of products we deal in and the type of services we provide. Purpose is to convince the prospective client to engage our services and also to sell us their scrap metal.
http://www.pelrowanmetals.com/our-services/for-corporate <- This link is for the intended audience of this brochure.
Designer is welcome to take any images from my website or use their own images in the design. Preferably, should the designer choose to use scrap metal images, please try to mainly use pictures of aluminium scrap, copper scrap, stainless steel scrap and ferrous scrap.
Attached is our company logo and some pictures of the scrap. www.pelrowanmetals.com is our website.
The design should give the audience a feeling of confidence, professionalism, honesty and trust in us.
This brochure is intended to be A4 Sizer
Target Market(s)
Local manufacturing company that does metal fabrication with off-cut scrap during the manufacturing process
Industry/Entity Type
Steel
Look and feel

```html
<!DOCTYPE html>
<html lang="en">
<head>
<meta charset="utf-8">
<title>About Us – Pelrowan Metals Recycling</title>
<link rel="stylesheet" href="https://fonts.googleapis.com/css2?family=Oswald:wght@200;300;400&display=swap">
<style>
  :root {
    --paper: #ffffff;
    --ink: #1e1e1e;
    --body-ink: #3a3a3a;
    --copper-dark: #5a3322;
    --copper: #a4644a;
    --copper-light: #d79a7c;
    --gold: #c9a24a;
    --gold-light: #f1dca0;
    --gold-dark: #9c7a2e;
  }
  * { margin: 0; padding: 0; box-sizing: border-box; }
  html, body { width: 848px; height: 1200px; overflow: hidden; background: var(--paper); }
  .page {
    position: relative;
    width: 848px;
    height: 1200px;
    background: var(--paper);
    font-family: "Oswald", "Arial Narrow", sans-serif;
    color: var(--ink);
  }
  .hero-photo {
    position: absolute;
    left: 0; top: 0;
    width: 848px; height: 326px;
    background: linear-gradient(170deg, var(--copper-dark) 0%, var(--copper) 35%, var(--copper-light) 60%, var(--copper) 80%, var(--copper-dark) 100%);
  }
  .gold-rule {
    position: absolute;
    left: 0; top: 326px;
    width: 848px; height: 9px;
    background: linear-gradient(90deg, var(--gold-dark) 0%, var(--gold-light) 30%, var(--gold) 55%, var(--gold-light) 80%, var(--gold-dark) 100%);
  }
  .about-title {
    position: absolute;
    left: 53px; top: 422px;
    font-weight: 300;
    font-size: 60px;
    line-height: 1;
    letter-spacing: -0.5px;
    transform: scaleX(0.8);
    transform-origin: left top;
    color: var(--ink);
  }
  .about-body {
    position: absolute;
    left: 54px; top: 527px;
    width: 742px;
    font-weight: 300;
    font-size: 15px;
    line-height: 28px;
    text-align: justify;
    color: var(--body-ink);
  }
  .about-body p + p { margin-top: 28px; }
  .brand {
    position: absolute;
    left: 520px; top: 999px;
    width: 276px;
    text-align: center;
  }
  .brand-mark {
    display: block;
    width: 70px; height: 70px;
    margin: 0 auto 12px;
    background: var(--gold);
  }
  .brand-name {
    font-weight: 400;
    font-size: 24px;
    line-height: 1.15;
    letter-spacing: 1.5px;
    color: var(--gold);
  }
</style>
</head>
<body>
  <main class="page">
    <div class="hero-photo" role="img" aria-label="Bundled copper wire scrap tied with steel wire"></div>
    <div class="gold-rule"></div>

    <h1 class="about-title">ABOUT US</h1>

    <section class="about-body">
      <p>Pelrowan Metals Recycling is a privately-held company located in Singapore with a humble beginning. We have grown rapidly through the continuous support of our customers and suppliers and currently have suppliers across various industries including the general public, construction, manufacturers, engineering, demolition, shipyards, other recycling yards and overseas customers.</p>
      <p>Pelrowan Metals Recycling has become a recycling industry leader in the local market, committed to responsibly and efficiently serving all its customers, suppliers and community with integrity and professionalism, and in an environmentally safe manner.</p>
      <p>We are committed to our suppliers and consumers by effectively sourcing, processing, and marketing scrap metal for recycling. We actively pursue new and long-lasting relationships by partnering with our customers, providing quality service built upon integrity, honesty, and professionalism. We are committed to meeting all our customers' needs by exceeding their expectations.</p>
    </section>

    <div class="brand">
      <span class="brand-mark"></span>
      <div class="brand-name">PELROWAN METALS<br>RECYCLING</div>
    </div>
  </main>
</body>
</html>
```